Elegant invitation for prestigious fund raising event

Background
The Lanterns of Grace is a very prestigious fund raising event. It is a sit down dinner, gala type evening with a presentation and auction.
There are three of these event being held at venues around western North Carolina. The areas where these are being held all have one thing in common, they are in the Appalachian Mountains and the craft of quilt making. As you will see from the Concept Boards attached why a mountain theme and quilt “design feel” is being used. One very important point - we don’t want this design to look like an actual quilt.

See the concept board on page 4, which we can’t use that is from another artist but is one good interpretation of the idea and one way to stylize the picture with a “quilt” interpretation and feel. We do not want a literal quilt representation but are looking for an artistic way on how best to interpret what the quilt represents - the feel of “stitching together” the different things across our region that make us all unique but yet bind us all as one.

The Brief:
We want to develop an elegant invitation for these events.
We have develop as save the date (attached) and all we want to use of this is the wording “Lanterns of Grace” we do not like the icon above it.
Also attached is the wording for the invitation, along with the new picture we want to use (taken from the inspiration boards)

Size, fold, color and paper:

Around 5x7 inches, but open to any dimension if you have an idea that will work in a totally different size. Ideally try and stick to something that will fit a standard envelope so that we don’t need to make a special envelope

Fold – up to you if it has a fold or not and which way it folds. Our thought is that it will need a fold to keep it up market but open to any suggestions.
We are happy to print this on a textured paper if you have suggestions. It will be professionally digital printed so the paper needs to be suitable for digital printing

Color. The inspiration boards show the color palette. We have started out in the save the dates with the navy with reversed out white but again totally up to you to use anything from that color palette.
Updates

Target Market(s)

Up market, around 50 - 65 years old, many are retired, very wealthy

Industry/Entity Type

Event

Requirements
Must have
• See brief attached
Nice to have
• See brief attached
Should not have
• See brief attached

```html
<!DOCTYPE html>
<html lang="en">
<head>
<meta charset="utf-8">
<title>Lanterns of Grace – Invitation</title>
<link href="https://fonts.googleapis.com/css2?family=Archivo+Narrow:ital,wght@0,500;1,500&family=Cinzel:wght@400;600&family=Lobster&family=Raleway:wght@300;400&display=swap" rel="stylesheet">
<style>
  :root {
    --page: #f1f0f4;
    --navy: #1f3f8f;
    --royal: #3556b8;
    --sky: #4a7fd0;
    --violet: #6b4fb0;
    --magenta: #c95aa8;
    --peach: #e8a27e;
    --sunset: #f0a23a;
    --forest: #2c4a2a;
    --pine: #48652f;
    --ink: #1e2150;
    --white: #ffffff;
  }
  * { box-sizing: border-box; margin: 0; padding: 0; }
  html, body { width: 976px; height: 1200px; overflow: hidden; }
  body { background: var(--page); position: relative; font-family: "Archivo Narrow", Arial, sans-serif; }

  /* ---------- Folded cover card ---------- */
  .cover {
    position: absolute; left: 40px; top: 70px;
    width: 420px; height: 600px;
    box-shadow: 0 6px 18px rgba(30, 33, 80, .18);
    overflow: hidden;
  }
  .cover__top {
    position: absolute; inset: 0 0 auto 0; height: 270px;
    background: radial-gradient(ellipse at 40% 30%, var(--sky), var(--royal) 55%, var(--navy));
  }
  .cover__scroll-art {
    position: absolute; left: 0; top: 0; width: 100%; height: 270px;
    background: linear-gradient(160deg, rgba(20, 40, 100, .35), rgba(20, 40, 100, 0) 45%, rgba(20, 40, 100, .25));
  }
  .cover__hospital {
    position: absolute; top: 28px; left: 0; right: 0;
    transform: rotate(180deg);
    transform-origin: center;
    text-align: center; color: var(--white);
    font-family: "Cinzel", Georgia, serif; font-weight: 600;
    display: flex; justify-content: center; align-items: center; gap: 10px;
  }
  .cover__hospital-mark { width: 12px; height: 12px; background: var(--white); }
  .cover__hospital-name { font-size: 17px; letter-spacing: 1px; }

  .cover__landscape {
    position: absolute; left: 0; right: 0; top: 270px; bottom: 0;
    background:
      linear-gradient(180deg, var(--sky) 0%, #8aa0c8 8%, var(--sunset) 18%, #d9884a 24%, #7e8fb8 32%, #6f86b8 42%, var(--pine) 55%, var(--forest) 100%);
  }
  .cover__fold {
    position: absolute; left: 0; right: 0; top: 270px;
    border-top: 1.5px dashed rgba(255, 255, 255, .85);
  }
  .cover__title {
    position: absolute; left: 150px; top: 440px; width: 230px;
    color: var(--white); text-align: center;
  }
  .cover__title-mark {
    width: 14px; height: 14px; border-radius: 50%;
    background: var(--white); margin: 0 auto 10px;
  }
  .cover__title-name {
    font-family: "Raleway", Arial, sans-serif; font-weight: 300;
    font-size: 26px; line-height: 1.15; letter-spacing: 1px; text-transform: uppercase;
  }
  .cover__title-rule {
    display: flex; align-items: center; gap: 8px; margin-top: 6px;
  }
  .cover__title-rule::before, .cover__title-rule::after {
    content: ""; flex: 1; border-top: 1.5px solid var(--white);
  }
  .cover__title-sub {
    font-family: "Cinzel", Georgia, serif; font-size: 17px; letter-spacing: 2px;
  }

  /* ---------- Invitation insert ---------- */
  .invite {
    position: absolute; left: 500px; top: 400px;
    width: 440px; height: 690px;
    box-shadow: 0 6px 18px rgba(30, 33, 80, .2);
    overflow: hidden; color: var(--ink);
  }
  .invite__wash {
    position: absolute; inset: 0;
    background: linear-gradient(180deg,
      var(--sky) 0%, var(--violet) 22%, var(--magenta) 38%,
      var(--peach) 50%, #b89bc0 62%, #6d78b8 78%, var(--royal) 100%);
  }
  .invite__frame { position: absolute; inset: 0; }
  .invite__content {
    position: absolute; left: 40px; right: 40px; top: 62px; bottom: 40px;
    text-align: center;
  }
  .invite__heading {
    display: inline-block;
    font-family: "Lobster", cursive; font-size: 30px; color: var(--white);
    border-bottom: 2px solid var(--white); padding: 0 4px 1px; line-height: 1.1;
  }
  .invite__intro {
    margin-top: 18px; font-style: italic; font-size: 15.5px; line-height: 36px;
  }
  .invite__details {
    margin-top: 120px; font-size: 15.5px; line-height: 36px; text-transform: uppercase;
  }
  .invite__details sup { font-size: 9px; }
  .invite__notes {
    margin-top: 8px; font-size: 15.5px; color: var(--white); text-transform: uppercase; letter-spacing: .3px;
  }
  .invite__footnote {
    margin-top: 14px; font-style: italic; font-size: 11px; color: var(--white);
  }
</style>
</head>
<body>

  <section class="cover" aria-label="Invitation cover">
    <div class="cover__top"></div>
    <div class="cover__scroll-art" role="img" aria-label="Textured blue paper with faint scrollwork flourishes"></div>
    <div class="cover__hospital">
      <span class="cover__hospital-mark"></span>
      <span class="cover__hospital-name">Ridgecrest Valley Hospital</span>
    </div>
    <div class="cover__landscape" role="img" aria-label="Painted Appalachian mountain sunset with pine trees in the foreground"></div>
    <div class="cover__fold"></div>
    <div class="cover__title">
      <div class="cover__title-mark"></div>
      <div class="cover__title-name">Lanterns of Grace</div>
      <div class="cover__title-rule"><span class="cover__title-sub">Plateau</span></div>
    </div>
  </section>

  <section class="invite" aria-label="Invitation card">
    <div class="invite__wash" role="img" aria-label="Watercolour wash of blue, violet, pink and peach over a misty mountain ridge"></div>
    <svg class="invite__frame" width="440" height="690" viewBox="0 0 440 690" aria-hidden="true">
      <path d="M28 18 H412 A10 10 0 0 0 422 28 V662 A10 10 0 0 0 412 672 H28 A10 10 0 0 0 18 662 V28 A10 10 0 0 0 28 18 Z"
            fill="none" stroke="#ffffff" stroke-width="1.5"/>
    </svg>
    <div class="invite__content">
      <h1 class="invite__heading">Invitation</h1>
      <p class="invite__intro">
        You are invited to<br>
        The Second Annual<br>
        LANTERNS OF GRACE on the plateau.<br>
        Please join us for an elegant and entertaining affair<br>
        benefiting the healthcare in our region.
      </p>
      <p class="invite__details">
        6<sup>th</sup> of June, 2016<br>
        The Farm at Laurel Creek Inn<br>
        Beginning at 5:30pm<br>
        Valet Parking
      </p>
      <p class="invite__notes">Cocktail Attire &nbsp;·&nbsp; Valet Parking</p>
      <p class="invite__footnote">All Proceeds From The Night Will Go To Benefit Ridgecrest Valley Hospital</p>
    </div>
  </section>

</body>
</html>
```